Finiding oppertunites in Real Estate 6.15.20

size of ad 7” x 9.6”
1-I like the ad to stand out and attract people's attention.
2-you should be able to see the text of the ad clearly .. see the attachment anything in yellow is instructions.
3-the list of topics should not be the main part of the ad
4-if you decide you want a picture or vector of a person .. (you decide)
then it should be a white male about 25-30 years old wearing a solid white or blue shirt and not long hair.
5-leave 1 inch for footer
see attachment
Good luck

Target Market(s)

potential male students 25-35 years of age

Industry/Entity Type

Education

Requirements
Must have
• will stand out and people would want to see it.
should be able to read the words of ad
Nice to have
• how to make money in real estate on one line

```html
<!DOCTYPE html>
<html lang="en">
<head>
<meta charset="UTF-8">
<title>Real Estate Career Course</title>
<link rel="stylesheet" href="https://fonts.googleapis.com/css2?family=Libre+Caslon+Text:wght@700&family=Montserrat:wght@400;500;600;700&display=swap">
<style>
  :root {
    --navy: #1e2462;
    --navy-text: #2b3380;
    --orange: #f07022;
    --amber: #f7a51c;
    --amber-deep: #f28a1f;
    --white: #ffffff;
    --ink: #1a1a1a;
    --photo-light: #8c8a78;
    --photo-dark: #2a2e36;
  }
  * { margin: 0; padding: 0; box-sizing: border-box; }
  html, body { width: 875px; height: 1200px; overflow: hidden; background: var(--white); }
  .flyer {
    position: relative;
    width: 875px;
    height: 1200px;
    overflow: hidden;
    background: var(--white);
    font-family: "Montserrat", Arial, sans-serif;
  }
  .shapes { position: absolute; inset: 0; }
  .title {
    position: absolute;
    left: 38px;
    top: 58px;
    color: var(--navy);
  }
  .title-main {
    font-family: "Libre Caslon Text", Georgia, serif;
    font-weight: 700;
    font-size: 52px;
    line-height: 1;
    letter-spacing: 0.5px;
  }
  .title-sub {
    font-weight: 500;
    font-size: 29px;
    letter-spacing: 5.5px;
    margin-top: 12px;
  }
  .info-panel {
    position: absolute;
    left: 0;
    top: 205px;
    width: 425px;
    height: 412px;
    background: var(--navy);
    padding: 24px 0 0 44px;
    font-weight: 700;
    font-size: 35px;
    line-height: 1.2;
  }
  .info-highlight { color: var(--amber); }
  .info-line { color: var(--white); margin-top: 26px; }
  .info-divider {
    height: 3px;
    width: 381px;
    background: var(--amber);
    margin-top: 16px;
  }
  .headline {
    position: absolute;
    left: 38px;
    top: 652px;
    font-family: "Libre Caslon Text", Georgia, serif;
    font-weight: 700;
    font-size: 31px;
    line-height: 1.12;
    color: var(--orange);
  }
  .lead {
    position: absolute;
    left: 38px;
    top: 740px;
    width: 640px;
    color: var(--navy-text);
    font-size: 29px;
    font-weight: 500;
    line-height: 1.25;
  }
  .lead p + p { margin-top: 14px; }
  .topics {
    position: absolute;
    left: 43px;
    top: 938px;
    color: var(--ink);
  }
  .topics-heading {
    font-size: 16px;
    font-weight: 700;
    letter-spacing: 0.5px;
  }
  .topics-columns {
    display: flex;
    margin-top: 10px;
    list-style: none;
  }
  .topics-columns ul { list-style: none; }
  .topics-columns ul:nth-child(1) { width: 248px; }
  .topics-columns ul:nth-child(2) { width: 252px; }
  .topics-columns li {
    font-size: 17px;
    line-height: 20.5px;
  }
</style>
</head>
<body>
<div class="flyer">
  <svg class="shapes" width="875" height="1200" viewBox="0 0 875 1200" xmlns="http://www.w3.org/2000/svg">
    <defs>
      <linearGradient id="photoTone" x1="0" y1="0" x2="1" y2="1">
        <stop offset="0" stop-color="var(--photo-light)"/>
        <stop offset="0.55" stop-color="#5a5c58"/>
        <stop offset="1" stop-color="var(--photo-dark)"/>
      </linearGradient>
      <clipPath id="canvasClip"><rect width="875" height="1200"/></clipPath>
    </defs>
    <g clip-path="url(#canvasClip)">
      <circle cx="640" cy="388" r="332" fill="var(--orange)"/>
      <circle cx="660" cy="372" r="314" fill="url(#photoTone)" role="img" aria-label="Photo of a smiling young man in a dark suit and tie holding a black clipboard outdoors"/>
      <circle cx="850" cy="1028" r="178" fill="var(--amber)"/>
      <circle cx="780" cy="1140" r="135" fill="var(--orange)"/>
    </g>
  </svg>

  <header class="title">
    <h1 class="title-main">REAL ESTATE</h1>
    <p class="title-sub">CAREER COURSE</p>
  </header>

  <section class="info-panel">
    <p class="info-highlight">REMOTE<br>SESSIONS</p>
    <p class="info-line">12 SESSION<br>COURSE</p>
    <div class="info-divider"></div>
    <p class="info-line" style="margin-top:18px">CLASSES<br>STARTING<br>JUNE 16</p>
  </section>

  <h2 class="headline">HOW TO MAKE<br>MONEY IN REAL ESTATE?</h2>

  <div class="lead">
    <p>For those who have started or would like to go into Real Estate</p>
    <p>An investment in knowledge opens up untold opportunities</p>
  </div>

  <section class="topics">
    <h3 class="topics-heading">A PARTIAL LISTING OF TOPICS:</h3>
    <div class="topics-columns">
      <ul>
        <li>Single-family</li>
        <li>Multifamily</li>
        <li>Management</li>
        <li>Real Estate Concepts</li>
        <li>Real Estate law</li>
      </ul>
      <ul>
        <li>Investment properties</li>
        <li>Foreclosures</li>
        <li>Rehab</li>
        <li>Foreclosures</li>
        <li>Short sales</li>
      </ul>
      <ul>
        <li>Development</li>
        <li>Finical modeling</li>
        <li>HUD properties</li>
        <li>Due Diligence e</li>
      </ul>
    </div>
  </section>
</div>
</body>
</html>
```